Multi-Line Insurance PPC Landing Page - Conversion optimized.

We have a PPC landing page used for the general population to get an insurance quote through an agent's site.

We'd like to improve the page for PPC traffic, make it more conversion friendly.

Site should be a single long page.

We will dynamically change the form and headlines on the page depending on what insurance "line" is being called. ie, Lift, Auto, Home, Business.

The enclosed AI file has all of the raw elements we need. We're looking to enhance the design and conversion ability.

Target Market(s)

General public needed insurance services.

Industry/Entity Type

Insurance Broker

Number of Pages Required

1 page

Font styles to use
Sans Serif

Requirements
Must have
• Form, agent picture, name, address.

```html
<!DOCTYPE html>
<html lang="en">
<head>
<meta charset="utf-8">
<title>Insurance Agent – Life Insurance Quote</title>
<link href="https://fonts.googleapis.com/css2?family=Open+Sans:ital,wght@0,400;0,600;0,700;1,400;1,600&display=swap" rel="stylesheet">
<style>
:root{
  --blue:#1f5aa8;
  --blue-dark:#17407f;
  --navy:#1b3a73;
  --green:#3b8a2c;
  --green-dark:#2e6f22;
  --grey-bg:#eef0f3;
  --line:#d4d8de;
  --text:#4a4f57;
  --muted:#7b818a;
  --white:#fff;
}
*{box-sizing:border-box;margin:0;padding:0}
html,body{width:1200px;height:2992px;overflow:hidden}
body{font-family:"Open Sans",Arial,sans-serif;color:var(--text);background:var(--white)}
.page{width:1200px;height:2992px;position:relative}

/* header */
.site-header{height:120px;display:flex;justify-content:space-between;align-items:center;background:var(--white);position:relative}
.brand{height:120px;background:var(--blue);color:var(--white);font-weight:700;font-size:36px;display:flex;align-items:center;padding:0 90px 0 40px;clip-path:polygon(0 0,100% 0,86% 100%,0 100%)}
.header-phone{display:flex;align-items:center;gap:16px;padding-right:40px}
.phone-icon{width:56px;height:56px;border-radius:50%;background:var(--green);display:flex;align-items:center;justify-content:center}
.header-phone small{display:block;font-size:17px;color:var(--muted)}
.header-phone strong{font-size:28px;color:#2a2f36}

/* hero */
.hero{height:520px;position:relative;background:linear-gradient(180deg,#9cc6ea 0%,#cfe3f2 45%,#8fb35a 68%,#5e8a2e 100%)}
.hero-copy{position:absolute;left:80px;top:140px}
.hero h1{font-size:64px;font-weight:600;color:var(--white);text-shadow:0 2px 6px rgba(0,0,0,.25)}
.btn{display:inline-block;background:var(--green);color:var(--white);font-weight:700;text-transform:uppercase;border-radius:4px;text-align:center;box-shadow:0 3px 0 var(--green-dark)}
.hero .btn{margin-top:48px;font-size:28px;padding:20px 38px}

/* quote */
.quote{height:432px;display:flex;gap:40px;padding:24px 80px 0;background:var(--white)}
.agent-card{width:330px;height:380px;background:#f6f7f9;border:1px solid var(--line);text-align:center;padding-top:22px}
.agent-photo{width:190px;height:190px;border-radius:50%;margin:0 auto;border:6px solid var(--blue);background:linear-gradient(180deg,#d9dde2,#7a8796)}
.agent-card h3{font-size:24px;margin-top:18px;color:#2a2f36}
.agent-card .tel{font-size:22px;font-weight:600;margin-top:6px;display:flex;justify-content:center;align-items:center;gap:8px}
.agent-card address{font-style:normal;font-size:18px;margin-top:12px;line-height:1.4}
.quote-form{flex:1}
.quote-form h2{font-size:30px;font-weight:600;color:#2a2f36;margin-bottom:14px}
.quote-form h2 span{color:var(--blue)}
.form-grid{display:grid;grid-template-columns:1fr 1fr;column-gap:40px;row-gap:12px}
.field label{display:block;font-size:15px;margin-bottom:4px}
.input{height:32px;border:1px solid var(--line);background:var(--white);font-size:14px;color:#9aa0a8;padding:6px 10px}
.selects{display:flex;gap:10px}
.selects .input{flex:1}
.submit{margin-top:16px;font-size:18px;padding:8px 30px}

/* about */
.about{height:200px;text-align:center;padding:10px 80px 0}
.section-title{font-size:34px;font-weight:600;color:var(--blue);display:flex;align-items:center;justify-content:center;gap:20px}
.section-title b{color:#2a2f36;font-weight:600}
.section-title::before,.section-title::after{content:"";width:60px;height:2px;background:var(--line)}
.about p{font-size:17px;line-height:1.6;margin-top:16px}

/* products */
.products{height:888px;background:var(--grey-bg);padding-top:36px}
.cards{display:grid;grid-template-columns:repeat(3,320px);gap:38px 60px;justify-content:center;margin-top:36px}
.card{background:var(--white);height:366px;box-shadow:0 2px 6px rgba(0,0,0,.12);text-align:center;position:relative}
.card-head{height:58px;background:var(--blue);color:var(--white);font-size:22px;font-weight:600;display:flex;align-items:flex-end;justify-content:center;padding-bottom:8px;border-radius:8px 8px 0 0;position:relative}
.card-icon{position:absolute;top:-20px;left:50%;transform:translateX(-50%);width:46px;height:46px;border-radius:50%;background:var(--blue);border:4px solid var(--white)}
.card-photo{height:130px;margin:10px}
.card p{font-size:14px;line-height:1.5;padding:4px 18px}
.card .btn{font-size:15px;padding:8px 22px;margin-top:10px}

/* reviews */
.reviews{height:360px;padding-top:40px}
.review-list{display:flex;justify-content:center;gap:60px;margin-top:40px}
.review{display:flex;gap:20px;width:490px}
.review-photo{width:110px;height:110px;border-radius:50%;flex:none;background:linear-gradient(180deg,#e5e7ea,#8b95a2);border:4px solid var(--line)}
.review-box{background:#f3f4f6;padding:16px 20px;font-size:15px;line-height:1.5;position:relative}
.review-name{font-style:italic;font-weight:600;color:var(--blue);font-size:17px;margin-top:14px}

/* companies */
.companies{height:240px;border-top:1px solid var(--line);padding-top:30px}
.logo-row{display:flex;align-items:center;justify-content:center;gap:44px;margin-top:40px}
.arrow{width:40px;height:40px;background:var(--blue);display:flex;align-items:center;justify-content:center}
.partner{font-size:26px;font-weight:700;color:#3a3f46}

/* footer */
.site-footer{height:232px;background:var(--navy);color:#cfd7e6;padding:26px 80px 0;position:relative}
.footer-top{display:flex;justify-content:space-between}
.disclaimer{width:720px}
.disclaimer h4{color:var(--white);font-size:18px;margin-bottom:8px}
.disclaimer p{font-size:14px;line-height:1.5}
.footer-contact{text-align:right;color:var(--white)}
.footer-contact strong{font-size:24px;display:block}
.footer-contact span{font-size:15px;line-height:1.4;display:block;margin-top:6px}
.footer-brand{position:absolute;right:80px;bottom:48px;font-size:42px;font-weight:600;color:#c5d2ea}
.copyright{position:absolute;left:80px;bottom:22px;font-size:14px}
</style>
</head>
<body>
<div class="page">

<header class="site-header">
  <div class="brand">Insurance Agent</div>
  <div class="header-phone">
    <div class="phone-icon"><svg width="28" height="28" viewBox="0 0 24 24"><path fill="#fff" d="M6.6 10.8a15.1 15.1 0 0 0 6.6 6.6l2.2-2.2c.3-.3.7-.4 1-.2 1.1.4 2.3.6 3.6.6.6 0 1 .4 1 1V20c0 .6-.4 1-1 1A17 17 0 0 1 3 4c0-.6.4-1 1-1h3.5c.6 0 1 .4 1 1 0 1.3.2 2.5.6 3.6.1.3 0 .7-.2 1z"/></svg></div>
    <div><small>Get a quick quote by phone</small><strong>(555) 014-2270</strong></div>
  </div>
</header>

<section class="hero" role="img" aria-label="Family playing together in a sunny grassy field under a blue sky">
  <div class="hero-copy">
    <h1>Life Insurance</h1>
    <a class="btn">Get a Quote!</a>
  </div>
</section>

<section class="quote">
  <aside class="agent-card">
    <div class="agent-photo" role="img" aria-label="Portrait of the insurance agent in a suit"></div>
    <h3>Marcus Hale - Agent</h3>
    <div class="tel"><svg width="18" height="18" viewBox="0 0 24 24"><path fill="#1f5aa8" d="M6.6 10.8a15.1 15.1 0 0 0 6.6 6.6l2.2-2.2c.3-.3.7-.4 1-.2 1.1.4 2.3.6 3.6.6.6 0 1 .4 1 1V20c0 .6-.4 1-1 1A17 17 0 0 1 3 4c0-.6.4-1 1-1h3.5c.6 0 1 .4 1 1 0 1.3.2 2.5.6 3.6.1.3 0 .7-.2 1z"/></svg>(555) 014-2270</div>
    <address>418 Harbor Lane<br>Riverton, CA 90417</address>
  </aside>
  <div class="quote-form">
    <h2>Get An Instant <span>Insurance Quote.</span></h2>
    <div class="form-grid">
      <div class="field"><label>Full Name :</label><div class="input"></div></div>
      <div class="field"><label>Height/Weight :</label><div class="input"></div></div>
      <div class="field"><label>Sex :</label><div class="input">Select</div></div>
      <div class="field"><label>Tobacco Use :</label><div class="input">Select</div></div>
      <div class="field"><label>Date of Birth :</label><div class="selects"><div class="input">Month</div><div class="input">Day</div><div class="input">Year</div></div></div>
      <div class="field"><label>Phone :</label><div class="input"></div></div>
      <div class="field"><label>Current Health :</label><div class="input">Select</div></div>
      <div class="field"><label>Email :</label><div class="input"></div></div>
    </div>
    <a class="btn submit">Submit</a>
  </div>
</section>

<section class="about">
  <h2 class="section-title"><span>About <b>Insurance Agent</b></span></h2>
  <p>Lorem ipsum dolor sit amet, consectetuer adipiscing elit, sed diam nonummy nibh euismod tincidunt ut laoreet dolore magna aliquam erat volutpat. Ut wisi enim ad minim veniam, quis nostrud exerci tation ullamcorper suscipit lobortis nisl ut aliquip ex ea commodo consequat. Duis autem vel eum iriure dolor in hendrerit in vulputate velit esse molestie consequat, vel illum dolore eu feugiat nulla facilisis at vero eros et accumsan et iusto odio dignissim qui blandit praesent.</p>
</section>

<section class="products">
  <h2 class="section-title"><span>Our <b>Insurance</b> Products</span></h2>
  <div class="cards">
    <article class="card"><div class="card-head"><i class="card-icon"></i>Auto Insurance</div><div class="card-photo" role="img" aria-label="Person holding car keys" style="background:linear-gradient(135deg,#4a5b72,#1f2a3a)"></div><p>Lorem ipsum dolor sit amet, consectetuer adipiscing elit, sed diam nonummy nibh euismod tincidunt ut laoreet dolore magna aliquam erat</p><a class="btn">Get a Quote</a></article>
    <article class="card"><div class="card-head"><i class="card-icon"></i>Home Insurance</div><div class="card-photo" role="img" aria-label="Hands holding a small model house" style="background:linear-gradient(135deg,#e6d3c2,#b5463c)"></div><p>Lorem ipsum dolor sit amet, consectetuer adipiscing elit, sed diam nonummy nibh euismod tincidunt ut laoreet dolore magna aliquam erat</p><a class="btn">Get a Quote</a></article>
    <article class="card"><div class="card-head"><i class="card-icon"></i>Life Insurance</div><div class="card-photo" role="img" aria-label="Family outdoors on a sunny day" style="background:linear-gradient(180deg,#bcd8ef,#7fa24a)"></div><p>Lorem ipsum dolor sit amet, consectetuer adipiscing elit, sed diam nonummy nibh euismod tincidunt ut laoreet dolore magna aliquam erat</p><a class="btn">Get a Quote</a></article>
    <article class="card"><div class="card-head"><i class="card-icon"></i>Health Insurance</div><div class="card-photo" role="img" aria-label="Heartbeat line with a stethoscope" style="background:linear-gradient(135deg,#f4f4f4,#c9302c)"></div><p>Lorem ipsum dolor sit amet, consectetuer adipiscing elit, sed diam nonummy nibh euismod tincidunt ut laoreet dolore magna aliquam erat</p><a class="btn">Get a Quote</a></article>
    <article class="card"><div class="card-head"><i class="card-icon"></i>Business Insurance</div><div class="card-photo" role="img" aria-label="Business people under umbrellas" style="background:linear-gradient(180deg,#e9b774,#2c2c34)"></div><p>Lorem ipsum dolor sit amet, consectetuer adipiscing elit, sed diam nonummy nibh euismod tincidunt ut laoreet dolore magna aliquam erat</p><a class="btn">Get a Quote</a></article>
    <article class="card"><div class="card-head"><i class="card-icon"></i>Disability Insurance</div><div class="card-photo" role="img" aria-label="Person in a wheelchair outdoors" style="background:linear-gradient(180deg,#7fb2e0,#3b5e8a)"></div><p>Lorem ipsum dolor sit amet, consectetuer adipiscing elit, sed diam nonummy nibh euismod tincidunt ut laoreet dolore magna aliquam erat</p><a class="btn">Get a Quote</a></article>
  </div>
</section>

<section class="reviews">
  <h2 class="section-title"><span>Our <b>Customer Review</b></span></h2>
  <div class="review-list">
    <div class="review">
      <div class="review-photo" role="img" aria-label="Customer portrait"></div>
      <div><div class="review-box">“Lorem ipsum dolor sit amet, consectetuer adipiscing elit, sed diam nonummy nibh euismod tincidunt ut laoreet dolore magna aliquam erat volutpat.”</div><div class="review-name">Mr. Owen Parker</div></div>
    </div>
    <div class="review">
      <div class="review-photo" role="img" aria-label="Customer portrait"></div>
      <div><div class="review-box">“Lorem ipsum dolor sit amet, consectetuer adipiscing elit, sed diam nonummy nibh euismod tincidunt ut laoreet dolore magna aliquam erat volutpat.”</div><div class="review-name">Miss. Clara Voss</div></div>
    </div>
  </div>
</section>

<section class="companies">
  <h2 class="section-title"><span><b>Insurance</b> Company</span></h2>
  <div class="logo-row">
    <span class="arrow"><svg width="16" height="16" viewBox="0 0 16 16"><path d="M11 2 5 8l6 6" stroke="#fff" stroke-width="3" fill="none"/></svg></span>
    <span class="partner">Lumencrest</span>
    <span class="partner">Oakmere</span>
    <span class="partner">Pinebrook</span>
    <span class="partner">Solvana</span>
    <span class="partner">Halcyra</span>
    <span class="arrow"><svg width="16" height="16" viewBox="0 0 16 16"><path d="M5 2l6 6-6 6" stroke="#fff" stroke-width="3" fill="none"/></svg></span>
  </div>
</section>

<footer class="site-footer">
  <div class="footer-top">
    <div class="disclaimer">
      <h4>Disclaimer</h4>
      <p>Lorem ipsum dolor sit amet, consectetuer adipiscing elit, sed diam nonummy nibh euismod tincidunt ut laoreet dolore magna aliquam erat volutpat. Ut wisi enim ad minim veniam, quis nostrud exerci tation ullamcorper suscipit lobortis nisl ut aliquip ex ea commodo consequat.</p>
    </div>
    <div class="footer-contact">
      <strong>(555) 014-2270</strong>
      <span>418 Harbor Lane<br>Riverton, CA 90417</span>
    </div>
  </div>
  <div class="footer-brand">Insurance Agent</div>
  <div class="copyright">© 2016 Insurance Agent. All Rights reserved.</div>
</footer>

</div>
</body>
</html>
```